Web site for Life Coaching Consultant

I require a website for a life coaching business. I have a Tidal Netware account which I set up last week. I will need to be able to add articles and testimonials. The design should communicate that RL Harbor Lanterns is there to help people breakdown personal barriers and that we are an advocate to help them achieve personal goals.
Updates

Reason: I have some designers just accepting my invitation to submit so to give them a few days to submit. I have been thrilled with the quality of the submissions Thank you.

Hi everyone

I am loving all your designs.  The only feedback I can get from people is that they feel that the runner makes the web page look like a personal coach rather than a life coach that helps people with relations, career, and personal road blocks.

Sorry                                   

Reason: Hi I have increased the deadline as there has been so many amazing designs and some of you have asked to fine tune your entries. I would like to take this opportunity to thank you all. It is going to be a tough decision. I have put a few more pictures on the project page hoping this will help

Hi I just wanted to thank you all for your great designs.  As I got so many good designs I have asked people to vote.  I will be in touch in the next day or 2.

Cheers

Target Market(s)

People with self esteem issues either woman or girls, people who want to goal set and need an advocate

Industry/Entity Type

Life Coaching

Colors
d2a4cc
e567a6

Requirements
Must have
• must have bio section, logo, articles page, affirmation section and testimonial page.

```html
<!DOCTYPE html>
<html lang="en">
<head>
<meta charset="utf-8">
<title>Harbor Lanterns – Life Coaching</title>
<link href="https://fonts.googleapis.com/css2?family=Arimo:wght@400;700&family=Yellowtail&display=swap" rel="stylesheet">
<style>
:root{
  --pink:#e8136f;
  --pink-soft:#e567a6;
  --ink:#222;
  --text:#333;
  --muted:#666;
  --card:#efefef;
  --rule:#c9c9c9;
  --nav-top:#4a4a4a;
  --nav-bottom:#262626;
  --footer:#d9d9d9;
  --white:#fff;
}
*{margin:0;padding:0;box-sizing:border-box}
html,body{width:1200px;height:752px;overflow:hidden;background:var(--white)}
body{font-family:"Arimo",Arial,sans-serif;color:var(--text);position:relative}
a{color:inherit;text-decoration:none}

.top-rule{position:absolute;left:0;top:0;width:1200px;height:3px;background:#ddd}

.brand{position:absolute;left:272px;top:8px;display:flex;flex-direction:column;align-items:center;width:120px}
.brand-mark{width:52px;height:52px;border-radius:50%;background:var(--pink)}
.brand-name{margin-top:6px;font-size:17px;font-weight:700;color:var(--pink);white-space:nowrap}

.tagline{position:absolute;left:738px;top:30px;font-family:"Yellowtail",cursive;font-size:29px;color:var(--pink)}

.main-nav{position:absolute;left:0;top:94px;width:1200px;height:26px;background:linear-gradient(var(--nav-top),var(--nav-bottom))}
.main-nav ul{list-style:none;position:relative;height:26px}
.main-nav li{position:absolute;top:0;height:26px;line-height:26px;font-size:13px;color:var(--white)}
.main-nav li.active{background:var(--pink);padding:0 25px;left:259px}

.hero{position:absolute;left:0;top:120px;width:1200px;height:241px;
  background:linear-gradient(180deg,#a9d9ea 0%,#cfeaf3 45%,#e7f4f8 80%,#c8e3ec 100%)}
.hero-figure{position:absolute;left:480px;top:18px;width:120px;height:223px;
  background:linear-gradient(180deg,rgba(40,40,40,.55),rgba(30,30,30,.75));border-radius:40px 40px 6px 6px}
.hero-slogan{position:absolute;left:280px;top:42px;color:#111;line-height:1;font-weight:400}
.hero-slogan span{display:block;font-weight:400}
.hero-slogan .l1{font-size:40px;margin-left:20px}
.hero-slogan .l2{font-size:42px;font-weight:700;color:var(--pink);margin-top:2px;letter-spacing:-1px}
.hero-slogan .l3{font-size:26px;margin-top:2px}
.hero-slogan .l3 b{color:var(--pink);font-weight:700}
.hero-slogan .l4{font-size:40px;margin-left:25px}
.hero-box{position:absolute;left:625px;top:42px;width:307px;height:136px;background:var(--pink);color:var(--white);padding:12px 14px 0 18px}
.hero-box h2{font-size:19px;font-weight:400;line-height:23px}
.hero-box p{font-size:13px;line-height:19px;margin-top:12px}
.hero-rule{position:absolute;left:0;top:361px;width:1200px;height:5px;background:#cfcfcf}

.welcome{position:absolute;left:259px;top:376px;width:684px}
.welcome h1{font-size:20px;font-weight:400;color:var(--ink)}
.welcome h1 span{color:var(--pink)}
.welcome p{margin-top:8px;font-size:9.6px;line-height:16.2px;color:var(--text)}

.btn{display:inline-block;background:var(--pink);color:var(--white);font-size:8.5px;line-height:14px;padding:0 7px}
.welcome-more{position:absolute;left:871px;top:499px}

.card{position:absolute;top:521px;height:180px;background:var(--card);padding:12px 15px 0 15px}
.card-articles{left:258px;width:217px}
.card-affirm{left:491px;width:218px}
.card-testi{left:724px;width:218px;padding:12px 12px 0 12px}
.card-head{display:flex;align-items:center;gap:6px;height:26px}
.card-icon{width:26px;height:26px;display:block}
.card-head h3{font-size:15px;font-weight:400;color:var(--ink)}
.card .btn{position:absolute;bottom:10px;right:15px}

.article{padding:7px 0 6px;border-bottom:1px solid var(--rule);font-size:8.5px;line-height:12px}
.article + .article{border-bottom:0}
.article h4{font-size:9.5px;color:var(--pink);font-weight:700}
.article .meta{color:var(--muted)}
.article .meta b{font-weight:400;color:var(--text)}

.affirmations{list-style:none;margin-top:4px}
.affirmations li{display:flex;gap:6px;font-size:8.5px;line-height:12px;padding:6px 0 7px;border-bottom:1px solid var(--rule)}
.affirmations li span.arrow{color:var(--muted);flex:none}

.testimonial{display:flex;gap:10px;padding:5px 0 4px;font-size:8.5px;line-height:11px}
.testimonial + .testimonial{border-top:1px solid var(--rule)}
.testimonial p{white-space:nowrap}
.avatar{flex:none;width:44px;height:40px;margin-top:5px;background:linear-gradient(#d4d4d4,#c2c2c2)}
.testimonial h4{font-size:9.5px;line-height:11px;color:var(--pink)}

.site-footer{position:absolute;left:0;top:715px;width:1200px;height:37px;background:var(--footer);font-size:8.5px;color:#333}
.site-footer .copy{position:absolute;left:258px;top:15px}
.site-footer .links{position:absolute;right:258px;top:15px}
.site-footer .links span{margin:0 3px;color:#666}
</style>
</head>
<body>
<div class="top-rule"></div>

<header>
  <a class="brand" href="#">
    <span class="brand-mark"></span>
    <span class="brand-name">Harbor Lanterns</span>
  </a>
  <p class="tagline">“We help you get there”</p>
</header>

<nav class="main-nav">
  <ul>
    <li class="active">Home</li>
    <li style="left:361px">About us</li>
    <li style="left:455px">Articles</li>
    <li style="left:539px">Affirmation</li>
    <li style="left:642px">Testimonial</li>
    <li style="left:749px">Contact Us</li>
  </ul>
</nav>

<section class="hero">
  <div class="hero-figure" role="img" aria-label="Photo of a confident woman standing against a bright blue cloudy sky"></div>
  <h2 class="hero-slogan">
    <span class="l1">I am</span>
    <span class="l2">stronger</span>
    <span class="l3">than <b>any</b></span>
    <span class="l4">excuse.</span>
  </h2>
  <div class="hero-box">
    <h2>Lorem Ipsum is simply dummy text of the printing and</h2>
    <p>Typesetting industry. Lorem Ipsum has been the industry's standard dummy text ever since the 1500s, when an unknown printer</p>
  </div>
</section>
<div class="hero-rule"></div>

<section class="welcome">
  <h1>Welcome to <span>Harbor Lanterns</span></h1>
  <p>Lorem Ipsum is simply dummy text of the printing and typesetting industry. Lorem Ipsum has been the industry's standard dummy text ever since the 1500s, when an unknown printer took a galley of type and scrambled it to make a type specimen book. It has survived not only five centuries, but also the leap into electronic type-setting, remaining essentially unchanged. It was popularised in the 1960s with the release of Typeline sheets containing Lorem Ipsum passages, and more recently with desktop publishing software like Quill Layout including versions of Lorem Ipsum.Lorem Ipsum is simply dummy text of the printing and typesetting industry. Lorem Ipsum has been the industry's standard dummy text ever since the 1500s, when an unknown printer took a galley of type and scrambled it to make a type specimen book.</p>
</section>
<a class="btn welcome-more" href="#">Read More...</a>

<section class="card card-articles">
  <div class="card-head">
    <svg class="card-icon" viewBox="0 0 26 26" aria-hidden="true"><rect width="26" height="26" fill="#e8136f"/><rect x="7" y="5" width="12" height="16" fill="none" stroke="#fff" stroke-width="1.6"/><path d="M10 10h6M10 13h6M10 16h6" stroke="#fff" stroke-width="1.4"/></svg>
    <h3>Articles</h3>
  </div>
  <article class="article">
    <h4>Article title article title</h4>
    <div class="meta">by <b>DANA WELLS</b> &nbsp;January 28, 2014</div>
    <p>Lorem Ipsum is simply dummy text of the printing and typesetting industry.</p>
  </article>
  <article class="article">
    <h4>Article title article title</h4>
    <div class="meta">by <b>DANA WELLS</b> &nbsp;January 28, 2014</div>
    <p>Lorem Ipsum is simply dummy text of the printing and typesetting industry.</p>
  </article>
  <a class="btn" href="#">Read More...</a>
</section>

<section class="card card-affirm">
  <div class="card-head">
    <svg class="card-icon" viewBox="0 0 26 26" aria-hidden="true"><rect width="26" height="26" fill="#e8136f"/><circle cx="13" cy="13" r="6" fill="none" stroke="#fff" stroke-width="1.8"/><path d="M10 13l2 2 4-4" fill="none" stroke="#fff" stroke-width="1.6"/></svg>
    <h3>Affirmation</h3>
  </div>
  <ul class="affirmations">
    <li><span class="arrow">→</span><span>I am the architect of my life; I build its foundation and choose its contents.</span></li>
    <li><span class="arrow">→</span><span>Lorem Ipsum is simply dummy text of the printing and typesetting industry.</span></li>
    <li><span class="arrow">→</span><span>I am the architect of my life; I build its foundation and choose its contents.</span></li>
  </ul>
  <a class="btn" href="#">Read More...</a>
</section>

<section class="card card-testi">
  <div class="card-head">
    <svg class="card-icon" viewBox="0 0 26 26" aria-hidden="true"><rect width="26" height="26" fill="#e8136f"/><path d="M5 6h16v10H12l-4 4v-4H5z" fill="none" stroke="#fff" stroke-width="1.6"/></svg>
    <h3>Testimonial</h3>
  </div>
  <div class="testimonial">
    <div class="avatar" role="img" aria-label="Client portrait placeholder"></div>
    <div><h4>Name</h4><p>Lorem Ipsum is simply dummy text of<br>the printing and typesetting industry.<br>Lorem Ipsum has been the</p></div>
  </div>
  <div class="testimonial">
    <div class="avatar" role="img" aria-label="Client portrait placeholder"></div>
    <div><h4>Name</h4><p>Lorem Ipsum is simply dummy text of<br>the printing and typesetting industry.<br>Lorem Ipsum has been the</p></div>
  </div>
  <a class="btn" href="#">Read More...</a>
</section>

<footer class="site-footer">
  <p class="copy">Copyright © 2014 Harbor Lanterns. All rights reserved.</p>
  <p class="links">Home<span>|</span>About us<span>|</span>Articles<span>|</span>Affirmation<span>|</span>Testimonial<span>|</span>Contact Us</p>
</footer>
</body>
</html>
```